Speisekarten-Design für Gastronomiebetrieb
Zielgruppe
Wir sind ein Gastronomiebetrieb in einer Studentenstadt. Unsere Hauptzielgruppe sind junge Menschen und Studenten, aber auch älteres Puplikum. Wir möchten gerne ein neues Speisekartendesign, da unser aktuelles seit über 10 Jahren sich kaum verändert hat.
Aufgabenstellung
Gerne könne Sie sich die aktulle Speisekarte auf der unserer Hompeage anschauen: www.tomello-kassel.de
Auf der Frontseite soll die Farbrichtung Orange und natürlich das Logo beibehalten werden. Für die restlichen Seiten gibt es diese Einschränkung nicht. Uns ist wichtig, dass die Speisekarte modern, bunt und peppig ist. Das heisst möglichst mit kräftigen Farben und Bildern von Speisen und Getränken arbeiten.

```html
<!DOCTYPE html>
<html lang="de">
<head>
<meta charset="utf-8">
<title>Tomello – Speisekarte Titelseite</title>
<link rel="stylesheet" href="https://fonts.googleapis.com/css2?family=Oswald:wght@500;600&display=swap">
<style>
  :root {
    --backdrop: #e4e3e2;
    --orange-light: #f4955c;
    --orange-deep: #eb7430;
    --red-light: #e26e60;
    --red-deep: #d9534a;
    --brand-red: #c8302b;
    --tagline-yellow: #f6c23c;
    --spine-line: #5a2a1c;
    --frame-white: #fbfaf8;
  }
  * { margin: 0; padding: 0; box-sizing: border-box; }
  html, body {
    width: 1200px;
    height: 900px;
    overflow: hidden;
    background: var(--backdrop);
  }
  .menu-cover {
    position: absolute;
    left: 200px;
    top: 50px;
    width: 800px;
    height: 800px;
    overflow: hidden;
    background: linear-gradient(90deg, var(--red-light), var(--red-deep));
    font-family: 'Oswald', sans-serif;
  }
  .cover-top-band {
    position: absolute;
    inset: 0;
    background: linear-gradient(90deg, var(--orange-light), var(--orange-deep));
    clip-path: polygon(0 0, 100% 0, 100% 300px, 0 376px);
  }
  .spine-line {
    position: absolute;
    left: 19px;
    top: 0;
    width: 1.5px;
    height: 100%;
    background: var(--spine-line);
    opacity: 0.75;
  }
  .brand-name {
    position: absolute;
    left: 0;
    right: 0;
    top: 92px;
    text-align: center;
    padding-left: 16px;
    font-size: 96px;
    font-weight: 600;
    letter-spacing: 8px;
    color: var(--brand-red);
    line-height: 1;
  }
  .tagline {
    position: absolute;
    left: 0;
    right: 0;
    top: 226px;
    text-align: center;
    padding-left: 16px;
    font-size: 27px;
    font-weight: 500;
    letter-spacing: 2px;
    color: var(--tagline-yellow);
    word-spacing: 10px;
  }
  .photo-frame {
    position: absolute;
    background: var(--frame-white);
    padding: 22px;
    box-shadow: 0 2px 6px rgba(90, 30, 20, 0.25);
  }
  .photo-frame--salad {
    left: 44px;
    top: 530px;
    width: 300px;
    height: 300px;
    transform: rotate(-8deg);
  }
  .photo-frame--peppers {
    left: 408px;
    top: 468px;
    width: 350px;
    height: 360px;
    transform: rotate(3deg);
  }
  .photo-fill {
    width: 100%;
    height: 100%;
  }
  .photo-fill--salad {
    background: linear-gradient(150deg, #e9a27a 0%, #8fbf5a 35%, #f0c79a 60%, #d9d46a 100%);
  }
  .photo-fill--peppers {
    background: linear-gradient(135deg, #d3231f 0%, #e8c030 30%, #c81d1b 55%, #f2c43a 80%, #d82a22 100%);
  }
</style>
</head>
<body>
  <main class="menu-cover">
    <div class="cover-top-band"></div>
    <div class="spine-line"></div>
    <h1 class="brand-name">TOMELLO</h1>
    <p class="tagline">CAFÉ | BAR | RESTAURANT</p>
    <figure class="photo-frame photo-frame--salad">
      <div class="photo-fill photo-fill--salad" role="img" aria-label="Nahaufnahme eines bunten Salats mit Brokkoli und Gemüse"></div>
    </figure>
    <figure class="photo-frame photo-frame--peppers">
      <div class="photo-fill photo-fill--peppers" role="img" aria-label="Rote und gelbe Paprikaschoten in Nahaufnahme"></div>
    </figure>
  </main>
</body>
</html>
```